Webdesign für Versicherungsmakler
Zielgruppe
Wir sind ein Versicherungsmakler und wollen unseren Internetauftritt modernisieren. Unsere Zielgruppe sind mittelständische Unternehmen. Wir erstellen neben den Sachversicherungen und der Altersvororge auch versicherungsmathematische Gutachten. Wir beraten, erstellen Angebote und verwalten und betreuen die Versicherungsverträge und Schadenfälle unserer Kunden.
Aufgabenstellung
Es besteht bereits eine Website: https://www.k-und-r.example/. An dieser sollte sich orientiert werden, die Inhalte werden vermutlich in Zukunft Ähnlich bleiben.
Der Aufbau der Website soll modernisiert werden. Das Logo soll erhalten bleiben. Die Seite soll einen modernen, cleanen und dennoch zuverlässigen Eindruck vermitteln.

```html
<!DOCTYPE html>
<html lang="de">
<head>
<meta charset="utf-8">
<title>Kessler &amp; Rautenberg – Versicherungsmakler für Unternehmen</title>
<link href="https://fonts.googleapis.com/css2?family=Nunito+Sans:wght@300;400;600;700;800&display=swap" rel="stylesheet">
<style>
  :root {
    --blue: #0d5a94;
    --blue-dark: #0b4f86;
    --orange: #e07a5f;
    --hero-bg: #f5f5f5;
    --text: #555555;
    --grey: #6b6b6b;
    --border: #e3e3e3;
    --white: #ffffff;
  }
  * { margin: 0; padding: 0; box-sizing: border-box; }
  html, body { width: 1200px; height: 1071px; overflow: hidden; background: var(--white); }
  body { position: relative; font-family: "Nunito Sans", Arial, sans-serif; color: var(--text); }

  .site-header { position: absolute; left: 0; top: 0; width: 1200px; height: 107px; background: var(--white); }
  .brand { position: absolute; left: 56px; top: 28px; display: flex; align-items: center; gap: 12px; }
  .brand-mark { width: 50px; height: 50px; background: var(--blue); }
  .brand-divider { width: 1px; height: 52px; background: #999; }
  .brand-name { font-size: 22px; font-weight: 300; color: var(--grey); line-height: 25px; letter-spacing: 1px; text-transform: uppercase; }

  .main-nav { position: absolute; top: 36px; left: 387px; font-size: 19px; color: var(--blue); }
  .main-nav a { color: inherit; text-decoration: none; position: absolute; white-space: nowrap; }
  .btn { display: flex; align-items: center; justify-content: center; background: var(--orange); color: var(--white); font-weight: 700; border-radius: 7px; text-decoration: none; }
  .btn-header { position: absolute; left: 980px; top: 31px; width: 120px; height: 43px; font-size: 19px; }

  .hero { position: absolute; left: 0; top: 107px; width: 1200px; height: 489px; background: var(--hero-bg); overflow: hidden; }
  .hero-visual { position: absolute; left: 0; top: 0; }
  .hero-title { position: absolute; left: 56px; top: 116px; color: var(--blue); }
  .hero-title .light { display: block; font-size: 37px; font-weight: 300; line-height: 46px; }
  .hero-title .bold { display: block; font-size: 40px; font-weight: 800; line-height: 50px; margin-left: 12px; }
  .hero-text { position: absolute; left: 66px; top: 218px; width: 420px; font-size: 14px; line-height: 24.4px; color: var(--text); white-space: nowrap; }
  .btn-hero { position: absolute; left: 72px; top: 360px; width: 175px; height: 44px; font-size: 21px; }
  .slider-dots { position: absolute; left: 578px; top: 469px; display: flex; gap: 5px; }
  .slider-dots span { width: 12px; height: 12px; border-radius: 50%; border: 1px solid var(--blue); }
  .slider-dots .active { background: var(--orange); border-color: var(--orange); }

  .welcome { position: absolute; left: 0; top: 640px; width: 1200px; text-align: center; }
  .welcome h2 { font-size: 19px; font-weight: 800; color: var(--blue-dark); margin-left: -30px; }
  .welcome p { font-size: 9.5px; line-height: 12.5px; color: var(--text); margin-top: 14px; }

  .service-card { position: absolute; top: 732px; width: 273px; height: 290px; border: 1px solid var(--border); background: var(--white); }
  .service-illustration { position: absolute; top: 43px; height: 115px; border-radius: 6px; background: linear-gradient(135deg, #dce8f2, #c6d9ea 70%, #f1d2c8); }
  .service-title { position: absolute; top: 203px; left: 0; width: 100%; text-align: center; font-size: 15.5px; font-weight: 700; color: var(--blue); line-height: 21px; }
  .service-title.two-line { text-align: left; left: 45px; }
</style>
</head>
<body>
  <header class="site-header">
    <div class="brand">
      <div class="brand-mark"></div>
      <div class="brand-divider"></div>
      <div class="brand-name">Kessler<br>&amp; Rautenberg</div>
    </div>
    <nav class="main-nav">
      <a href="#" style="left:0">Home</a>
      <a href="#" style="left:84px">Profil</a>
      <a href="#" style="left:161px">Dienstleistungen</a>
      <a href="#" style="left:339px">Unternehmen</a>
      <a href="#" style="left:494px">Service</a>
    </nav>
    <a class="btn btn-header" href="#">Kontakt</a>
  </header>

  <section class="hero">
    <svg class="hero-visual" width="1200" height="489" viewBox="0 0 1200 489">
      <defs>
        <linearGradient id="photo-tone" x1="0" y1="0" x2="1" y2="1">
          <stop offset="0" stop-color="#2f5f8f"/>
          <stop offset="0.5" stop-color="#5f8ab3"/>
          <stop offset="1" stop-color="#9ab6cf"/>
        </linearGradient>
      </defs>
      <polygon points="701,0 1200,0 1200,489 701,489 584,243" fill="var(--orange)"/>
      <polygon role="img" aria-label="Foto: moderne Bürohochhäuser mit Glasfassaden, blau getönt, mit großem Schutzschild-Symbol" points="713,0 1200,0 1200,489 713,489 597,243" fill="url(#photo-tone)"/>
    </svg>
    <h1 class="hero-title"><span class="light">Versicherungsmakler</span><span class="bold">für Unternehmen</span></h1>
    <p class="hero-text">is simply dummy text of the printing and typesetting industry.<br>Lorem Ipsum has been the industry’s standard dummy text<br>ever since the 1500s, when an unknown printer took a galley of<br>type and scrambled it to make a type specimen book. It has<br>survived not only five centuries, but also the leap into electronic</p>
    <a class="btn btn-hero" href="#">Kontakt</a>
    <div class="slider-dots"><span class="active"></span><span></span><span></span></div>
  </section>

  <section class="welcome">
    <h2>Willkommen bei Kessler &amp; Rautenberg</h2>
    <p>Experten für Ihr Versicherungsmanagement und betriebliche Altersversorgung<br>unabhängiger Versicherungsmakler</p>
  </section>

  <article class="service-card" style="left:128px">
    <div class="service-illustration" role="img" aria-label="Illustration: Lupe mit Zahnrad, Schutzschild und Kalender" style="left:65px;width:118px"></div>
    <h3 class="service-title">Versicherungsmanagement</h3>
  </article>
  <article class="service-card" style="left:418px">
    <div class="service-illustration" role="img" aria-label="Illustration: Checkliste mit älterer Person am Gehstock" style="left:86px;width:100px"></div>
    <h3 class="service-title">Altersvorsorge</h3>
  </article>
  <article class="service-card" style="left:708px">
    <div class="service-illustration" role="img" aria-label="Illustration: Schutzschild, Karte und steigendes Balkendiagramm" style="left:70px;width:110px"></div>
    <h3 class="service-title two-line">Versicherungsmathematische<br>&nbsp;Gutachten</h3>
  </article>
</body>
</html>
```